Personalized Technology Company Needs a Business Card

I need a double-sided business card. Both sides will have the logo, and the contact information. One side will be black, with the white / gray logo, and the other will be white, with the black / gray logo. The black side will have the text "Custom Gaming PC's" and will have a water-cooled gaming PC image. The white side will have the text "Custom Business Computers & Consulting", and will have a business / enterprise PC image. Feel free to add a conservative image in the background, while the color remains unchanged. I'm uploading the base logo (transparent), so you can modify the colors, both the finished colored logos and an idea of ​​the business card (with the current information, just missing the website, which is www.volinexsystems.com, please add it.) Thank you so much for your effort, I'll be specting your cool designs. Good Luck!

Target Market(s)

Gamers & Entrepreneurs / Business Owners / Chief Technology Officers

Industry/Entity Type

Technology Equipment

Contact Information for Business Card

I need a double-sided business card. Both sides will have the logo, and the contact information. One side will be black, with the white/gray logo, and the other one will be white, with the black/gray logo. The black side will have the text "Custom Gaming PC's" and will have a water-cooled gaming PC image. The white side will have the text "Custom Business Computers & Consulting", and will have a business/enterprise PC image. Feel free to add a conservative image in the background, whilst the color remains unchanged.

I'm uploading the base logo (transparent), so you can modify the colors, both the finished colored logos and an idea of the business card (with the actual information, just missing the website, which is www.volinexsystems.com, please add it.)

Thank you so much for your effort, I'll be specting your cool designs. Good Luck!

Font styles to use
Serif

Colors
000000
757575
ffffff

Requirements
Must have
• Please See Description
Nice to have
• Please See Description
Should not have
• Please See Description

```html
<!DOCTYPE html>
<html lang="en">
<head>
<meta charset="utf-8">
<title>Volinex Systems – Business Cards</title>
<link rel="stylesheet" href="https://fonts.googleapis.com/css2?family=Jost:wght@400;500;600&display=swap">
<style>
  :root {
    --page: #ffffff;
    --card-dark: #232a33;
    --card-light: #ffffff;
    --accent-blue: #1a48e2;
    --sand-light: #e0d6c8;
    --sand-dark: #c8baa7;
    --sand: #c9bcab;
    --ink: #111111;
    --paper-text: #ffffff;
    --muted: #9a948c;
    --card-edge: #d9d9d9;
  }
  html, body {
    margin: 0;
    width: 1200px;
    height: 1200px;
    overflow: hidden;
    background: var(--page);
    font-family: "Jost", "Futura", sans-serif;
  }
  .sheet {
    position: relative;
    width: 1200px;
    height: 1200px;
  }
  .card {
    position: absolute;
    left: 221px;
    width: 757px;
    height: 444px;
    display: block;
  }
  .card--front { top: 118px; }
  .card--back  { top: 624px; }
  .card text { font-family: "Jost", "Futura", sans-serif; }
  .brand-name { font-weight: 600; font-size: 25px; letter-spacing: 2.5px; }
  .person-name { font-weight: 500; font-size: 19px; }
  .person-role { font-weight: 400; font-size: 13px; }
  .contact-line { font-weight: 400; font-size: 14.5px; }
  .tagline { font-weight: 500; font-size: 22px; }
  .website { font-weight: 400; font-size: 19px; }
</style>
</head>
<body>
<main class="sheet">

  <!-- Dark side -->
  <svg class="card card--front" viewBox="0 0 631 370" xmlns="http://www.w3.org/2000/svg">
    <defs>
      <linearGradient id="gaming-pc-tone" x1="0" y1="0" x2="1" y2="1">
        <stop offset="0" stop-color="#e9edf5"/>
        <stop offset="0.5" stop-color="#4f7de6"/>
        <stop offset="1" stop-color="#1b2440"/>
      </linearGradient>
    </defs>
    <rect class="card-face" width="631" height="370" fill="var(--card-dark)"/>
    <polygon class="accent-band" points="470,0 631,0 631,300" fill="var(--accent-blue)"/>
    <g class="peak">
      <polygon points="476,0 311,318 476,310" fill="var(--sand-light)"/>
      <polygon points="476,0 476,310 631,302" fill="var(--sand-dark)"/>
    </g>
    <line class="accent-rule" x1="466" y1="0" x2="310" y2="300" stroke="var(--accent-blue)" stroke-width="1.5"/>

    <g class="brand">
      <rect x="40" y="80" width="12" height="12" fill="var(--paper-text)"/>
      <text class="brand-name" x="60" y="95" fill="var(--paper-text)">VOLINEX SYSTEMS</text>
    </g>

    <text class="person-name" x="40" y="194" fill="var(--paper-text)">Ramon Ibarra <tspan fill="var(--accent-blue)">Soto</tspan></text>
    <text class="person-role" x="40" y="214" fill="var(--muted)">(CEO &amp; Co-Founder)</text>

    <g class="contact" fill="var(--paper-text)">
      <path d="M41 259 l3 -1 l2 4 l-2 1.5 q1.5 3 4 4.5 l1.5 -2 l4 2 l-1 3 q-8 0 -11.5 -12z" fill="var(--accent-blue)"/>
      <text class="contact-line" x="60" y="271">+52 5812 3390</text>
      <rect x="43" y="282" width="7" height="12" rx="1.5" fill="none" stroke="var(--accent-blue)" stroke-width="1.6"/>
      <text class="contact-line" x="60" y="294">+52 55 4681 0375</text>
      <rect x="41" y="309" width="11" height="8" fill="var(--accent-blue)"/>
      <polyline points="41,309 46.5,314 52,309" fill="none" stroke="var(--card-dark)" stroke-width="1"/>
      <text class="contact-line" x="60" y="317">contact@volinexsystems.com</text>
    </g>

    <g role="img" aria-label="Photo of a water-cooled custom gaming PC tower with blue lighting">
      <rect x="393" y="108" width="163" height="154" rx="4" fill="url(#gaming-pc-tone)"/>
    </g>
    <text class="tagline" x="476" y="300" text-anchor="middle" fill="var(--paper-text)">Custom Gaming PC's</text>

    <line x1="0" y1="340" x2="335" y2="340" stroke="var(--accent-blue)" stroke-width="1.5"/>
    <line x1="618" y1="340" x2="631" y2="340" stroke="var(--accent-blue)" stroke-width="1.5"/>
    <text class="website" x="477" y="346" text-anchor="middle" fill="var(--paper-text)">www.<tspan fill="var(--accent-blue)">volinexsystems</tspan>.com</text>
  </svg>

  <!-- Light side -->
  <svg class="card card--back" viewBox="0 0 631 370" xmlns="http://www.w3.org/2000/svg">
    <defs>
      <linearGradient id="business-pc-tone" x1="0" y1="0" x2="1" y2="1">
        <stop offset="0" stop-color="#5a86e0"/>
        <stop offset="0.55" stop-color="#cfd6e2"/>
        <stop offset="1" stop-color="#2a2d33"/>
      </linearGradient>
    </defs>
    <rect class="card-face" x="0.5" y="0.5" width="630" height="369" fill="var(--card-light)" stroke="var(--card-edge)"/>
    <polygon class="accent-band" points="470,0 631,0 631,300" fill="var(--accent-blue)"/>
    <g class="peak">
      <polygon points="476,0 311,318 476,310" fill="var(--sand-light)"/>
      <polygon points="476,0 476,310 631,302" fill="var(--sand-dark)"/>
    </g>
    <line class="accent-rule" x1="466" y1="0" x2="310" y2="300" stroke="var(--accent-blue)" stroke-width="1.5"/>

    <g class="brand">
      <rect x="40" y="80" width="12" height="12" fill="var(--ink)"/>
      <text class="brand-name" x="60" y="95" fill="var(--ink)">VOLINEX SYSTEMS</text>
    </g>

    <text class="person-name" x="40" y="194" fill="var(--ink)">Ramon Ibarra <tspan fill="var(--accent-blue)">Soto</tspan></text>
    <text class="person-role" x="40" y="214" fill="var(--sand)">(CEO &amp; Co-Founder)</text>

    <g class="contact" fill="var(--ink)">
      <path d="M41 259 l3 -1 l2 4 l-2 1.5 q1.5 3 4 4.5 l1.5 -2 l4 2 l-1 3 q-8 0 -11.5 -12z" fill="var(--accent-blue)"/>
      <text class="contact-line" x="60" y="271">+52 5812 3390</text>
      <rect x="43" y="282" width="7" height="12" rx="1.5" fill="none" stroke="var(--accent-blue)" stroke-width="1.6"/>
      <text class="contact-line" x="60" y="294">+52 55 4681 0375</text>
      <rect x="41" y="309" width="11" height="8" fill="var(--accent-blue)"/>
      <polyline points="41,309 46.5,314 52,309" fill="none" stroke="var(--card-light)" stroke-width="1"/>
      <text class="contact-line" x="60" y="317">contact@volinexsystems.com</text>
    </g>

    <g role="img" aria-label="Photo of a business desktop computer with monitor, tower, keyboard and mouse">
      <rect x="372" y="66" width="242" height="168" rx="4" fill="url(#business-pc-tone)"/>
    </g>
    <text class="tagline" x="478" y="284" text-anchor="middle" fill="var(--ink)">Custom Business</text>
    <text class="tagline" x="478" y="310" text-anchor="middle" fill="var(--ink)">Computers &amp; Consulting</text>

    <line x1="0" y1="340" x2="335" y2="340" stroke="var(--accent-blue)" stroke-width="1.5"/>
    <line x1="618" y1="340" x2="631" y2="340" stroke="var(--accent-blue)" stroke-width="1.5"/>
    <text class="website" x="477" y="346" text-anchor="middle" fill="var(--ink)">www.<tspan fill="var(--accent-blue)">volinexsystems</tspan>.com</text>
  </svg>

</main>
</body>
</html>
```